TUEW - Tally Up Every Week

We need a business card design for a company located in Australia - accounting / tax firm.

2 sided business card - I have attached a one-sided concept that I did in MSWord :) If anything it shows that I want a striking design - bold, fresh and less reserved than your average accounting firm's card.

Rather than having all the info on the front, maybe it could just have name and logo on front?

Want to keep colours in line with logo - orange, black and white.

Happy for full colour. Will be using a matte finish.

About Us (below)
TUEW does business, and more specifically accounting and taxation differently.
People require news and other media at their fingertips so why should business figures and documents be any different?
In combination with Xero, a cloud based accounting package, we store all receipts, tax returns and special documentation with a secure online data-storage provider and provide you with your own login. We are also interested to hear if video conferencing is something you would be interested in.
Using this technology we are able to focus more on your business and less on the data entry.

Target Market(s)

Individual mum and dad clients, and Small to Medium Business

Industry/Entity Type

Accounting

Requirements
Must have
• Must be able to edit the details at a future point in time ie - phone, address, website address, name on card and slogan.

2 sided

Standard Australian business card size
Nice to have
• Rather than having all the info on the front, maybe it could just have name and logo on front?
Should not have
• Don't want "Tally Up Every Week" on the card

```html
<!DOCTYPE html>
<html lang="en">
<head>
<meta charset="utf-8">
<title>TUEW – Business Card</title>
<link href="https://fonts.googleapis.com/css2?family=Open+Sans:wght@400;600&display=swap" rel="stylesheet">
<style>
  :root {
    --stage: #d8d9db;
    --card-front: #2b2b2e;
    --card-front-swoosh: #3a3a3e;
    --card-back: #151922;
    --orange: #f07f1a;
    --orange-light: #f9b233;
    --orange-deep: #c9560d;
    --white: #ffffff;
    --grey-text: #d6d6d6;
  }
  * { margin: 0; padding: 0; box-sizing: border-box; }
  html, body {
    width: 1200px;
    height: 900px;
    overflow: hidden;
    background: var(--stage);
    font-family: "Open Sans", Arial, sans-serif;
  }
  .canvas {
    position: relative;
    width: 1200px;
    height: 900px;
  }
  .card {
    position: absolute;
    left: 290px;
    width: 620px;
    height: 378px;
    overflow: hidden;
    border-radius: 4px;
    box-shadow: 0 6px 18px rgba(0,0,0,0.18);
  }

  /* Brand side */
  .card--brand { top: 52px; background: var(--card-front); }
  .brand-swoosh {
    position: absolute;
    left: 100px; top: -300px;
    width: 600px; height: 600px;
    border-radius: 50%;
    background: var(--card-front-swoosh);
  }
  .brand-sun {
    position: absolute;
    left: 130px; top: -241px;
    width: 520px; height: 520px;
    border-radius: 50%;
    background: radial-gradient(circle at 45% 62%, var(--orange-light) 0%, var(--orange) 38%, var(--orange-deep) 100%);
  }
  .brand-block {
    position: absolute;
    left: 66px; top: 150px;
    color: var(--white);
    text-align: right;
  }
  .brand-name {
    font-size: 44px;
    font-weight: 400;
    letter-spacing: 1px;
    line-height: 1;
  }
  .brand-services {
    margin-top: 10px;
    font-size: 14px;
    line-height: 1.35;
    color: var(--grey-text);
  }
  .brand-web {
    position: absolute;
    right: 40px; bottom: 30px;
    font-size: 17px;
    color: var(--orange);
  }

  /* Contact side */
  .card--contact { top: 470px; background: var(--card-back); }
  .person {
    position: absolute;
    left: 60px; top: 62px;
  }
  .person-name {
    font-size: 24px;
    color: var(--orange);
    line-height: 1.1;
  }
  .person-role {
    font-size: 13px;
    color: var(--white);
    letter-spacing: 0.5px;
  }
  .contact-list {
    list-style: none;
    margin-top: 22px;
    font-size: 15px;
    color: var(--white);
  }
  .contact-list li {
    display: flex;
    align-items: center;
    gap: 9px;
    margin-bottom: 5px;
  }
  .icon { width: 12px; height: 12px; fill: var(--orange); flex: none; }
  .firm {
    position: absolute;
    left: 344px; top: 118px;
    display: flex;
    align-items: center;
    gap: 16px;
  }
  .firm-text { text-align: right; color: var(--white); }
  .firm-name { font-size: 30px; line-height: 1; letter-spacing: 1px; }
  .firm-services { margin-top: 6px; font-size: 11px; line-height: 1.3; color: var(--grey-text); }
  .firm-mark {
    width: 112px; height: 112px;
    border-radius: 50%;
    background: radial-gradient(circle at 55% 35%, var(--orange-light) 0%, var(--orange) 45%, var(--orange-deep) 100%);
  }
  .address {
    position: absolute;
    left: 290px; top: 268px;
    display: flex;
    gap: 8px;
    font-size: 16px;
    line-height: 1.35;
    color: var(--white);
  }
  .address .icon { margin-top: 3px; width: 13px; height: 15px; }
</style>
</head>
<body>
<main class="canvas">

  <section class="card card--brand" aria-label="Business card, brand side">
    <div class="brand-swoosh"></div>
    <div class="brand-sun" role="img" aria-label="Large orange sun-like circle decoration"></div>
    <div class="brand-block">
      <p class="brand-name">TUEW</p>
      <p class="brand-services">Bookkeeping<br>Accounting<br>Taxation</p>
    </div>
    <p class="brand-web">www.tuew.com.au</p>
  </section>

  <section class="card card--contact" aria-label="Business card, contact side">
    <div class="person">
      <p class="person-name">Dana Merrick</p>
      <p class="person-role">TAX AGENT</p>
      <ul class="contact-list">
        <li>
          <svg class="icon" viewBox="0 0 12 12" aria-hidden="true"><rect x="2.5" y="0.5" width="7" height="11" rx="1.2"/><rect x="4" y="2" width="4" height="6.5" fill="#151922"/></svg>
          0412 555 018
        </li>
        <li>
          <svg class="icon" viewBox="0 0 12 12" aria-hidden="true"><rect x="0.5" y="2.5" width="11" height="7" rx="0.8"/><path d="M1 3 L6 7 L11 3" stroke="#151922" stroke-width="1" fill="none"/></svg>
          merrick@tuew.com.au
        </li>
      </ul>
    </div>

    <div class="firm">
      <div class="firm-text">
        <p class="firm-name">TUEW</p>
        <p class="firm-services">Bookkeeping<br>Accounting<br>Taxation</p>
      </div>
      <div class="firm-mark"></div>
    </div>

    <div class="address">
      <svg class="icon" viewBox="0 0 12 15" aria-hidden="true"><path d="M6 0 C2.7 0 0.5 2.4 0.5 5.3 C0.5 9 6 15 6 15 C6 15 11.5 9 11.5 5.3 C11.5 2.4 9.3 0 6 0 Z"/><circle cx="6" cy="5.3" r="2" fill="#151922"/></svg>
      <p>45 Sample Lane<br>Newtown, NSW 2042</p>
    </div>
  </section>

</main>
</body>
</html>
```